Cleaners Needs Bounce-Back Coupon For Laundry Service

We need a "bounce-back" coupon to attach to peoples dry cleaning orders that offers one free wash-n-fold laundry service. Right now we always attach their receipt to the bag that contains their dry cleaning when we return it. We'd like to also attach a coupon that will entice them to come try our laundry service.

Background on the service: We sort, wash, dry, and fold the laundry for customers and then neatly put it in a nice bag that makes returning very convenient. Their laundry comes out fresh, clean, smelling great, and without the hassle of doing it themselves. We have a great return rate. Most customers that try out the service become long term customers. The goal is to get our dry cleaning customers to come try it out.

Requirements:
* 5" x 8" and one-sided.
* To be printed on a standard color of card stock.
* Must incorporate our logo.
* Needs a place for us to fill in an expiration date. We'll fill in a date about two weeks out from the time they pick up their dry cleaning.
* Limit one coupon per customer.
* Limit 50 pounds of laundry per coupon.

```html
<!DOCTYPE html>
<html lang="en">
<head>
<meta charset="utf-8">
<title>Laundry on Elm – Free Wash-n-Fold Coupon</title>
<link rel="stylesheet" href="https://fonts.googleapis.com/css2?family=Archivo+Black&family=Fredoka:wght@500;600;700&display=swap">
<style>
  :root {
    --orange: #f26522;
    --royal: #2047a0;
    --navy: #1d3f95;
    --sky: #cfe6f7;
    --sky-deep: #8fc3ea;
    --white: #ffffff;
  }
  * { box-sizing: border-box; margin: 0; padding: 0; }
  html, body { width: 1200px; height: 750px; overflow: hidden; background: var(--white); }
  .coupon {
    position: relative;
    width: 1200px;
    height: 750px;
    overflow: hidden;
    background: var(--royal);
    font-family: "Fredoka", "Arial Rounded MT Bold", sans-serif;
  }
  .coupon__shapes { position: absolute; inset: 0; }

  .brand {
    position: absolute;
    left: 36px;
    top: 34px;
    display: flex;
    align-items: center;
    gap: 16px;
  }
  .brand__mark {
    width: 70px;
    height: 70px;
    background: var(--royal);
    border: 4px solid var(--white);
    border-radius: 6px;
  }
  .brand__name {
    font-weight: 600;
    font-size: 50px;
    color: var(--white);
    line-height: 1;
  }

  .expiry {
    position: absolute;
    right: 40px;
    top: 30px;
    width: 320px;
  }
  .expiry__label {
    font-family: "Archivo Black", "Arial Black", sans-serif;
    font-size: 19px;
    letter-spacing: 0.5px;
    color: var(--white);
    text-align: right;
    white-space: nowrap;
  }
  .expiry__fields {
    display: flex;
    align-items: center;
    gap: 12px;
    margin-top: 14px;
    justify-content: flex-end;
  }
  .expiry__day {
    width: 72px;
    height: 72px;
    border-radius: 50%;
    background: var(--white);
  }
  .expiry__year {
    width: 132px;
    height: 68px;
    background: var(--white);
    margin-left: 8px;
  }

  .offer {
    position: absolute;
    left: 156px;
    top: 270px;
    line-height: 0.92;
  }
  .offer__one, .offer__free, .offer__service { color: var(--orange); font-weight: 700; }
  .offer__one { font-size: 122px; margin-left: 30px; }
  .offer__free { font-size: 112px; letter-spacing: 2px; }
  .offer__service-name {
    display: block;
    color: var(--navy);
    font-weight: 700;
    font-size: 78px;
    margin-top: 18px;
    margin-left: 6px;
  }
  .offer__service { display: block; font-size: 60px; margin-top: 8px; }

  .terms {
    position: absolute;
    left: 668px;
    top: 664px;
    list-style: none;
    font-family: "Arial", sans-serif;
    font-size: 17px;
    line-height: 22px;
    color: var(--white);
  }
</style>
</head>
<body>
<main class="coupon">
  <svg class="coupon__shapes" width="1200" height="750" viewBox="0 0 1200 750">
    <path class="coupon__field" fill="var(--orange)"
      d="M0 0 H800 C815 120 960 160 990 260 L1040 640 C1050 710 1010 735 960 750 H0 Z"/>
    <path class="coupon__edge" fill="none" stroke="var(--white)" stroke-width="3"
      d="M814 0 C829 116 972 156 1004 258 L1054 640 C1064 716 1030 740 990 750"/>
    <!-- door hinges -->
    <rect x="700" y="370" width="120" height="62" rx="14" fill="var(--white)"/>
    <rect x="700" y="490" width="120" height="62" rx="14" fill="var(--white)"/>
    <rect x="700" y="384" width="100" height="34" rx="6" fill="var(--orange)"/>
    <rect x="700" y="504" width="100" height="34" rx="6" fill="var(--orange)"/>
    <!-- door -->
    <circle cx="358" cy="505" r="318" fill="var(--orange)" stroke="var(--white)" stroke-width="12"/>
    <defs>
      <radialGradient id="porthole" cx="0.45" cy="0.4" r="0.65">
        <stop offset="0" stop-color="var(--white)"/>
        <stop offset="0.6" stop-color="var(--sky)"/>
        <stop offset="1" stop-color="var(--sky-deep)"/>
      </radialGradient>
    </defs>
    <circle cx="362" cy="500" r="270" fill="url(#porthole)" stroke="var(--white)" stroke-width="10"
      role="img" aria-label="Washing machine window with swirling water and soap bubbles"/>
  </svg>

  <header class="brand">
    <span class="brand__mark"></span>
    <span class="brand__name">Laundry on Elm</span>
  </header>

  <section class="expiry">
    <p class="expiry__label">THIS OFFER GOOD THROUGH</p>
    <div class="expiry__fields">
      <span class="expiry__day"></span>
      <span class="expiry__day"></span>
      <span class="expiry__year"></span>
    </div>
  </section>

  <h1 class="offer">
    <span class="offer__one">One</span><br>
    <span class="offer__free">FREE</span>
    <span class="offer__service-name">wash-n-fold</span>
    <span class="offer__service">laundry service</span>
  </h1>

  <ul class="terms">
    <li>* Limit one coupon per customer.</li>
    <li>* Limit 50 pounds of laundry per coupon.</li>
  </ul>
</main>
</body>
</html>
```